Design a PowerPoint template for a consultancy organisation

I am after a Powerpoint template including three pages a title slide (that should have a title and subtitle), A title and content slide and a section header slide. I expect the company name and/or logo to be prominent and the colors to work well with the logo colors. I have included a copy of the logo

```html
<!DOCTYPE html>
<html lang="en">
<head>
<meta charset="utf-8">
<title>Civic Desk – Presentation Template</title>
<link href="https://fonts.googleapis.com/css2?family=Inter:wght@700;800&family=Montserrat:wght@500;600;700&display=swap" rel="stylesheet">
<style>
  :root {
    --stage: #bab8b9;
    --purple: #6a0dad;
    --green: #8dc63f;
    --green-bright: #7fd03a;
    --pale: #eef4e2;
    --white: #ffffff;
    --slate: #344a5a;
  }
  * { box-sizing: border-box; margin: 0; padding: 0; }
  html, body { width: 710px; height: 1200px; overflow: hidden; }
  body { background: var(--stage); position: relative; font-family: "Montserrat", Arial, sans-serif; }

  .slide { position: absolute; overflow: hidden; background: var(--purple); }
  .slide--title   { left: 41.6px; top: 46.4px;  width: 626.7px; height: 353px; }
  .slide--content { left: 45px;   top: 434.9px; width: 620px;   height: 348.7px; }
  .slide--section { left: 46px;   top: 817.6px; width: 622px;   height: 349.7px; }

  .slide-art { position: absolute; inset: 0; width: 100%; height: 100%; }

  .brand { position: absolute; display: flex; flex-direction: column; align-items: center; }
  .brand__mark { width: 24px; height: 24px; background: var(--purple); margin-bottom: 6px; }
  .brand__name { font-family: "Montserrat", Arial, sans-serif; font-weight: 600; font-size: 24px; color: var(--green); letter-spacing: -0.3px; line-height: 1; }

  .headline {
    position: absolute; left: 0; right: 0; text-align: center;
    font-family: "Inter", Arial, sans-serif; font-weight: 800; font-size: 42px; letter-spacing: -1.2px; line-height: 1;
  }
  .headline span {
    background: linear-gradient(90deg, var(--green) 0%, var(--green) 25%, var(--pale) 100%);
    -webkit-background-clip: text; background-clip: text; color: transparent;
  }
  .subtitle { position: absolute; left: 0; right: 0; top: 220px; text-align: center; font-size: 21.5px; font-weight: 500; color: var(--white); }
  .site-url { position: absolute; left: 0; right: 0; text-align: center; font-size: 11.5px; font-weight: 600; color: var(--white); letter-spacing: 0.2px; }

  .page-heading { position: absolute; left: 52px; top: 41px; font-size: 22px; font-weight: 700; letter-spacing: 0.3px; line-height: 1; }
  .page-heading span {
    background: linear-gradient(90deg, var(--green) 0%, var(--green) 35%, #6a2a9b 100%);
    -webkit-background-clip: text; background-clip: text; color: transparent;
  }
  .page-subheading { position: absolute; left: 50px; top: 69px; font-size: 15px; font-weight: 500; color: var(--purple); line-height: 1; }

  .corner-badge { position: absolute; left: 520px; top: 25px; width: 64px; height: 40px; background: var(--white); display: flex; align-items: center; justify-content: center; }
  .corner-badge .brand__name { font-size: 8.5px; color: var(--green); }

  .diagram-caption { position: absolute; left: 264px; width: 200px; top: 131px; text-align: center; font-size: 9.5px; font-weight: 500; color: var(--white); }

  .step { position: absolute; display: flex; align-items: center; justify-content: center; text-align: center; font-size: 9.5px; font-weight: 600; line-height: 1; }
  .step--outer { color: var(--slate); }
  .step--inner { color: var(--green-bright); }
</style>
</head>
<body>

  <!-- Title slide -->
  <section class="slide slide--title">
    <svg class="slide-art" viewBox="0 0 1310 738" preserveAspectRatio="none" aria-hidden="true">
      <circle cx="108" cy="-157" r="491" fill="var(--white)"/>
      <circle cx="1450" cy="880" r="483" fill="var(--green)"/>
    </svg>
    <div class="brand" style="left:50px; top:40px;">
      <div class="brand__mark"></div>
      <div class="brand__name">Civic Desk</div>
    </div>
    <h1 class="headline" style="top:178px;"><span>Marketing Strategy</span></h1>
    <p class="subtitle">Presentation Subtitle</p>
    <p class="site-url" style="top:312px;">www.company.com</p>
  </section>

  <!-- Title and content slide -->
  <section class="slide slide--content">
    <svg class="slide-art" viewBox="0 0 1296 729" preserveAspectRatio="none" aria-hidden="true">
      <defs>
        <g id="arrow-right">
          <circle cx="-11" cy="0" r="2.6" fill="var(--white)"/>
          <path d="M-4 -8 L11 0 L-4 8 L0 0 Z" fill="var(--white)"/>
        </g>
      </defs>
      <circle cx="106" cy="-158" r="487" fill="var(--white)"/>
      <circle cx="1420" cy="960" r="422" fill="var(--green)"/>

      <rect x="492" y="323" width="527" height="268" fill="none" stroke="var(--white)" stroke-width="3"/>

      <g fill="var(--white)" stroke="var(--green)" stroke-width="4">
        <rect x="71" y="423" width="123" height="76"/>
        <rect x="255" y="423" width="170" height="76"/>
        <rect x="1084" y="423" width="147" height="76"/>
      </g>
      <g fill="none" stroke="var(--green)" stroke-width="4">
        <rect x="526" y="355" width="199" height="72"/>
        <rect x="787" y="355" width="199" height="72"/>
        <rect x="526" y="485" width="199" height="73"/>
        <rect x="787" y="485" width="199" height="73"/>
      </g>

      <use href="#arrow-right" transform="translate(228 461)"/>
      <use href="#arrow-right" transform="translate(459 461)"/>
      <use href="#arrow-right" transform="translate(756 391)"/>
      <use href="#arrow-right" transform="translate(885 459) rotate(90)"/>
      <use href="#arrow-right" transform="translate(755 522) rotate(180)"/>
      <use href="#arrow-right" transform="translate(1054 461)"/>
    </svg>

    <h2 class="page-heading"><span>Warehousing</span></h2>
    <p class="page-subheading">Process</p>

    <div class="corner-badge"><span class="brand__name">Civic Desk</span></div>

    <p class="diagram-caption">Warehouse Process</p>

    <div class="step step--outer" style="left:34px; top:202.4px; width:58.8px; height:36.4px;">INPUT</div>
    <div class="step step--outer" style="left:122px; top:202.4px; width:81.3px; height:36.4px;">Recieving</div>
    <div class="step step--outer" style="left:518.6px; top:202.4px; width:70.3px; height:36.4px;">Shipping</div>

    <div class="step step--inner" style="left:251.6px; top:169.8px; width:95.2px; height:34.4px;">Check In</div>
    <div class="step step--inner" style="left:376.5px; top:169.8px; width:95.2px; height:34.4px;">Storage</div>
    <div class="step step--inner" style="left:251.6px; top:232px; width:95.2px; height:34.9px;">Shipping<br>preparation</div>
    <div class="step step--inner" style="left:376.5px; top:232px; width:95.2px; height:34.9px;">Order Picking</div>
  </section>

  <!-- Section header slide -->
  <section class="slide slide--section">
    <svg class="slide-art" viewBox="0 0 1300 731" preserveAspectRatio="none" aria-hidden="true">
      <circle cx="106" cy="-158" r="488" fill="var(--white)"/>
      <circle cx="1440" cy="870" r="478" fill="var(--green)"/>
    </svg>
    <div class="brand" style="left:50px; top:39px;">
      <div class="brand__mark"></div>
      <div class="brand__name">Civic Desk</div>
    </div>
    <h2 class="headline" style="top:187px;"><span>Section Title</span></h2>
    <p class="site-url" style="top:309px;">www.company.com</p>
  </section>

</body>
</html>
```